chocolate bar wrapper

Need a design for a new line of chocolate bars being sold at new retail candy store concept called PLIMBRAKES. There will be many flavors including Dark Chocolate, Milk Chocolate, Dark Chocolate Espresso, Milk Chocolate Smores, Dark Chocolate Strawberry Champagne, Dark Chocolate Sea Salt, Dark Chocolate Chipotle, etc. Size of bar is 3 inches x 6 5/8 inches.

Please visit PLIMBRAKES.COM

Industry/Entity Type

Retail

```html
<!DOCTYPE html>
<html lang="en">
<head>
<meta charset="UTF-8">
<title>Dark Chocolate Espresso – PLIMBRAKES Bar Wrapper</title>
<link rel="stylesheet" href="https://fonts.googleapis.com/css2?family=Alfa+Slab+One&display=swap">
<style>
  :root {
    --cocoa-light: #a87a4c;
    --cocoa-mid: #8a5f36;
    --cocoa-deep: #4a2e16;
    --ink-brown: #3a230f;
    --cream: #ffffff;
    --gold: #fff200;
    --brand-color: #e8dccb;
  }
  html, body {
    margin: 0;
    padding: 0;
    width: 1200px;
    height: 543px;
    overflow: hidden;
    background: var(--cocoa-mid);
  }
  .wrapper {
    position: relative;
    width: 1200px;
    height: 543px;
    overflow: hidden;
    font-family: "Alfa Slab One", Georgia, serif;
  }
  .wrapper__backdrop {
    position: absolute;
    inset: 0;
    background:
      radial-gradient(ellipse at 28% 30%, var(--cocoa-light) 0%, var(--cocoa-mid) 45%, var(--cocoa-deep) 100%);
  }
  .flavor-title {
    position: absolute;
    inset: 0;
    width: 1200px;
    height: 543px;
  }
  .flavor-title text {
    font-family: "Alfa Slab One", Georgia, serif;
    font-size: 98px;
    paint-order: stroke fill;
    stroke-linejoin: round;
  }
  .flavor-title .halo { fill: var(--gold); stroke: var(--gold); stroke-width: 22px; }
  .flavor-title .edge { fill: var(--cream); stroke: var(--ink-brown); stroke-width: 8px; }
  .brand {
    position: absolute;
    left: 522px;
    top: 352px;
    width: 600px;
    text-align: center;
  }
  .brand__name {
    margin: 0;
    font-size: 82px;
    line-height: 1;
    color: var(--brand-color);
    letter-spacing: 1px;
  }
  .brand__tagline {
    margin: 10px 0 0;
    font-size: 25px;
    line-height: 1;
    color: var(--ink-brown);
    letter-spacing: 0.5px;
  }
</style>
</head>
<body>
  <main class="wrapper">
    <div class="wrapper__backdrop" role="img" aria-label="Chocolate-brown sunburst of radiating rays"></div>

    <svg class="flavor-title" viewBox="0 0 1200 543" aria-label="Dark Chocolate Espresso">
      <g class="halo">
        <text x="48" y="158">Dark Chocolate</text>
        <text x="1082" y="282" text-anchor="end">Espresso</text>
      </g>
      <g class="edge">
        <text x="48" y="158">Dark Chocolate</text>
        <text x="1082" y="282" text-anchor="end">Espresso</text>
      </g>
    </svg>

    <div class="brand">
      <p class="brand__name">PLIMBRAKES</p>
      <p class="brand__tagline">ICE CREAM, CHOCOLATES &amp; CANDY!</p>
    </div>
  </main>
</body>
</html>
```